Design a A4 and DL Flyer

Design an A4 Flyer for our Job Tracking Software

Colors
f04a51
fffffe
fefafc
fbd4d5
fbd1d2

Requirements
Must have
• Task Relay by VENTRAHUB (logo attached) , maybe fancy Task Relay Words.

Packages File attached - also has list of features on the excel to the right.

Free 30 Day Trial
Free Support and Set Up assistance

PHONE: 1300 462 518
EMAIL: admin@ventrahub.com.au
Try now for free on our Demo Site: www.jobs.ventrahub.com.au
Nice to have
• Does you business provide a service or complete jobs for customers ?
Would you like to be able to track these jobs with ease?

```html
<!DOCTYPE html>
<html lang="en">
<head>
<meta charset="utf-8">
<title>Task Relay by VENTRAHUB – A4 Flyer</title>
<link href="https://fonts.googleapis.com/css2?family=Exo+2:wght@400;500;600&family=Lato:wght@400;700&display=swap" rel="stylesheet">
<style>
  :root {
    --brand-red: #f04a51;
    --deep-red: #e3242b;
    --ink: #111111;
    --panel-black: #0c0c0c;
    --paper: #fffffe;
    --paper-soft: #fefafc;
    --mist: #ececee;
    --grey-text: #555558;
    --pink-tint: #fbd4d5;
  }
  * { margin: 0; padding: 0; box-sizing: border-box; }
  html, body { width: 900px; height: 1200px; overflow: hidden; background: var(--paper); }
  .flyer {
    position: relative; width: 900px; height: 1200px; overflow: hidden;
    background: linear-gradient(180deg, var(--paper) 0%, var(--paper-soft) 100%);
    font-family: "Lato", Arial, sans-serif; color: var(--ink);
  }
  .office-backdrop {
    position: absolute; left: 0; top: 0; width: 900px; height: 1200px;
    background:
      radial-gradient(ellipse at 20% 75%, rgba(200,200,204,.35), transparent 45%),
      linear-gradient(180deg, #e2e3e6 0%, #f1f1f3 30%, rgba(255,255,255,.9) 45%, #f6f6f7 70%, #eeeeef 100%);
  }
  .swooshes { position: absolute; left: 0; top: 0; }
  .trial-badge {
    position: absolute; left: 200px; top: 50px; width: 284px; height: 284px;
    border-radius: 50%; background: var(--paper); border: 3px solid var(--ink);
    display: flex; align-items: center; justify-content: center;
  }
  .trial-badge__inner {
    width: 248px; height: 248px; border-radius: 50%; background: var(--deep-red);
    color: var(--paper); text-align: center; font-family: "Exo 2", Arial, sans-serif;
    display: flex; flex-direction: column; justify-content: center;
  }
  .trial-badge__small { font-size: 31px; font-weight: 500; line-height: 1.1; }
  .trial-badge__big { font-size: 50px; font-weight: 500; line-height: 1.05; }
  .photo-ring {
    position: absolute; left: 425px; top: 45px; width: 450px; height: 450px;
    border-radius: 50%; background: var(--paper); border: 12px solid var(--deep-red);
    padding: 8px;
  }
  .photo-ring__photo {
    width: 100%; height: 100%; border-radius: 50%;
    background: linear-gradient(135deg, #c9ced6 0%, #8e97a6 40%, #5d6f8d 70%, #b8c6da 100%);
  }
  .heading-font { font-family: "Exo 2", Arial, sans-serif; }
  .dot { display: inline-block; width: 16px; height: 16px; border-radius: 50%; }
  .dot--red { background: var(--brand-red); }
  .dot--black { background: var(--ink); }
  .support { position: absolute; left: 38px; top: 368px; }
  .support__title { display: flex; align-items: center; gap: 16px; font-size: 38px; font-weight: 500; letter-spacing: .5px; }
  .support__sub { margin-left: 55px; font-size: 26px; font-weight: 400; margin-top: 2px; }
  .support__rule { position: absolute; left: 90px; top: 470px; width: 203px; height: 3px; background: var(--brand-red); }
  .tier-left { position: absolute; left: 50px; }
  .tier-left__head { display: flex; align-items: center; gap: 22px; }
  .pill {
    display: inline-block; height: 38px; line-height: 38px; padding: 0 16px;
    border-radius: 0 6px 6px 0; color: var(--paper); font-size: 27px; font-weight: 500;
  }
  .pill--red { background: var(--deep-red); }
  .pill--black { background: var(--ink); }
  .features { list-style: none; margin-top: 8px; margin-left: 45px; }
  .features li { position: relative; padding-left: 16px; font-size: 14px; line-height: 21.6px; color: #222; }
  .features li::before {
    content: ""; position: absolute; left: 0; top: 7px; width: 7px; height: 7px;
    border-radius: 50%; background: var(--deep-red);
  }
  .call-bar {
    position: absolute; left: 38px; top: 1004px; width: 345px; height: 40px;
    background: var(--ink); color: var(--paper); border-radius: 0 8px 8px 0;
    font-family: "Exo 2", Arial, sans-serif; font-size: 26px; font-weight: 500;
    line-height: 40px; padding-left: 16px;
  }
  .brand-name {
    position: absolute; left: 55px; top: 1072px; display: flex; align-items: center; gap: 14px;
    font-family: "Lato", Arial, sans-serif; font-weight: 700; font-size: 40px; color: var(--grey-text);
  }
  .brand-name .dot { width: 34px; height: 34px; }
  .web-band { position: absolute; left: 0; bottom: 0; }
  .web-band__text {
    position: absolute; left: 42px; bottom: 10px; color: var(--paper);
    font-size: 19px; font-weight: 700; letter-spacing: 2.5px;
  }
  .pitch { position: absolute; left: 440px; width: 455px; text-align: center; }
  .pitch__lead { top: 535px; font-size: 17px; font-weight: 700; letter-spacing: .3px; }
  .pitch__big {
    top: 565px; font-family: "Exo 2", Arial, sans-serif; font-size: 34px; font-weight: 500;
    color: var(--deep-red); line-height: 42px;
  }
  .pitch__rule { position: absolute; left: 562px; top: 661px; width: 210px; height: 3px; background: var(--ink); }
  .question-bar {
    position: absolute; left: 443px; top: 678px; width: 457px; height: 33px;
    background: var(--deep-red); color: var(--paper); border-radius: 8px 0 0 8px;
    font-size: 15.5px; font-weight: 700; line-height: 33px; text-align: center;
  }
  .packages-panel {
    position: absolute; left: 435px; top: 732px; width: 465px; height: 383px;
    background: var(--panel-black); border-radius: 10px 0 0 10px; color: var(--paper);
  }
  .tier-right { position: absolute; left: 22px; }
  .tier-right__head {
    display: flex; align-items: center; gap: 18px; font-family: "Exo 2", Arial, sans-serif;
    font-size: 27px; font-weight: 500; color: var(--brand-red);
  }
  .tier-right__grid {
    list-style: none; display: grid; grid-template-columns: 192px 200px;
    grid-auto-flow: column; grid-template-rows: repeat(3, 21.5px); margin: 6px 0 0 16px;
  }
  .tier-right__grid li { position: relative; padding-left: 16px; font-size: 14px; line-height: 21.5px; }
  .tier-right__grid li::before {
    content: ""; position: absolute; left: 0; top: 7px; width: 7px; height: 7px;
    border-radius: 50%; background: var(--deep-red);
  }
  .mail-line { position: absolute; left: 470px; top: 1130px; width: 420px; text-align: center; font-size: 17px; font-weight: 700; }
</style>
</head>
<body>
<main class="flyer">
  <div class="office-backdrop" role="img" aria-label="Faded office scene with colleagues in the background"></div>

  <svg class="swooshes" width="900" height="1200" viewBox="0 0 900 1200" aria-hidden="true">
    <path d="M0,235 C250,140 600,170 900,395 L900,412 C600,200 250,190 0,280 Z" fill="#111111"/>
    <path d="M0,285 C250,205 600,225 900,418 L900,442 C600,262 260,255 0,365 Z" fill="#e3242b"/>
  </svg>

  <div class="photo-ring">
    <div class="photo-ring__photo" role="img" aria-label="Photo of two smiling businessmen shaking hands in an office"></div>
  </div>

  <div class="trial-badge">
    <div class="trial-badge__inner">
      <span class="trial-badge__small">FREE 30 DAY</span>
      <span class="trial-badge__big">TRIAL</span>
      <span class="trial-badge__big">POS</span>
    </div>
  </div>

  <section class="support heading-font">
    <div class="support__title"><span class="dot dot--red"></span>FREE SUPPORT</div>
    <div class="support__sub">and Set Up assistance</div>
  </section>
  <div class="support__rule"></div>

  <section class="tier-left" style="top:490px">
    <div class="tier-left__head"><span class="dot dot--black"></span><span class="pill pill--red heading-font">Unlimited Jobs</span></div>
    <ul class="features">
      <li>Job Management</li><li>Staff Scheduling</li><li>Quoting and Invoicing</li><li>No Point of Sale</li><li>No Automatic Statements</li>
    </ul>
  </section>

  <section class="tier-left" style="top:654px">
    <div class="tier-left__head"><span class="dot dot--black"></span><span class="pill pill--black heading-font">30 Jobs per month</span></div>
    <ul class="features">
      <li>Job Management</li><li>Staff Scheduling</li><li>No Quoting and Invoicing</li><li>No Point of Sale</li><li>No Automated Statements</li>
    </ul>
  </section>

  <section class="tier-left" style="top:820px">
    <div class="tier-left__head"><span class="dot dot--black"></span><span class="pill pill--red heading-font">50 Jobs per month</span></div>
    <ul class="features">
      <li>Job Management</li><li>Staff Scheduling</li><li>Quoting and Invoicing</li><li>No Point of Sale</li><li>Automated Statements</li>
    </ul>
  </section>

  <div class="call-bar">CALL US-1300 462 518</div>

  <div class="brand-name"><span class="dot dot--red"></span>VENTRAHUB</div>

  <svg class="web-band" width="900" height="48" viewBox="0 0 900 48" aria-hidden="true">
    <polygon points="0,0 480,0 510,48 0,48" fill="#e3242b"/>
    <polygon points="505,40 900,40 900,48 510,48" fill="#111111"/>
  </svg>
  <div class="web-band__text">www.jobs.ventrahub.com.au</div>

  <p class="pitch pitch__lead">DOES YOU BUSINESS PROVIDE A SERVICE OR</p>
  <h1 class="pitch pitch__big">COMPLETE JOBS FOR<br>CUSTOMERS ?</h1>
  <div class="pitch__rule"></div>
  <div class="question-bar">Would you like to be able to track these jobs with ease?</div>

  <section class="packages-panel">
    <div class="tier-right" style="top:28px">
      <div class="tier-right__head"><span class="dot dot--red"></span>150 Jobs per month</div>
      <ul class="tier-right__grid">
        <li>Job Management</li><li>Staff Scheduling</li><li>Quoting and Invoicing</li><li>No Point of Sale</li><li>Automated Statements</li>
      </ul>
    </div>
    <div class="tier-right" style="top:148px">
      <div class="tier-right__head"><span class="dot dot--red"></span>500 Jobs per month</div>
      <ul class="tier-right__grid">
        <li>Job Management</li><li>Staff Scheduling</li><li>Quoting and Invoicing</li><li>Point of Sale</li><li>Automated Statements</li>
      </ul>
    </div>
    <div class="tier-right" style="top:258px">
      <div class="tier-right__head"><span class="dot dot--red"></span>Unlimited Jobs</div>
      <ul class="tier-right__grid">
        <li>Job Management</li><li>Staff Scheduling</li><li>Quoting and Invoicing</li><li>Point of Sale</li><li>Automated Statements</li>
      </ul>
    </div>
  </section>

  <p class="mail-line">mail us-admin@ventrahub.com.au</p>
</main>
</body>
</html>
```